Hollow Fern Kentucky Bourbon Whiskey

We need a label design for a bottle of whiskey. It is for a 750 ml bottle and needs to have a place to write in proof, age, and bottle number at bottom of label. It is a single barrel bourbon. We want to include our tree logo attached in the upload files in some way. Leave out the Distillery part to where it just says Hollow Fern Bourbon Whiskey with the tree. We need the label to be clean and modern. I have also attached a picture of the bottle the label is intended to go on.

Industry/Entity Type

Bourbon

Requirements
Must have
• Hollow Fern tree from file

```html
<!DOCTYPE html>
<html lang="en">
<head>
<meta charset="UTF-8">
<title>Hollow Fern Kentucky Bourbon Whiskey – Label</title>
<link rel="stylesheet" href="https://fonts.googleapis.com/css2?family=Cinzel:wght@500&family=Rye&family=Roboto+Condensed:wght@400&display=swap">
<style>
  :root {
    --backdrop: #efece6;
    --gold-light: #f6dc7a;
    --gold-mid: #e2b83c;
    --gold-deep: #b98a1e;
    --maroon: #7b1d2a;
  }
  * { margin: 0; padding: 0; box-sizing: border-box; }
  html, body {
    width: 1200px;
    height: 1000px;
    overflow: hidden;
    background: var(--backdrop);
  }
  .canvas {
    position: relative;
    width: 1200px;
    height: 1000px;
  }
  .label {
    position: absolute;
    left: 240px;
    top: 160px;
    width: 720px;
    height: 680px;
    color: var(--maroon);
  }
  .label-shape {
    position: absolute;
    inset: 0;
    width: 720px;
    height: 680px;
  }
  .label-content {
    position: absolute;
    inset: 0;
    text-align: center;
  }
  .brand-mark {
    position: absolute;
    left: 325px;
    top: 70px;
    width: 70px;
    height: 70px;
    border-radius: 50%;
    background: var(--maroon);
  }
  .brand-name {
    position: absolute;
    left: 0;
    right: 0;
    top: 152px;
    font-family: "Cinzel", serif;
    font-weight: 500;
    font-size: 30px;
    letter-spacing: 1px;
  }
  .title {
    position: absolute;
    left: 0;
    right: 0;
    font-family: "Rye", serif;
    line-height: 1;
  }
  .title-kentucky { top: 224px; font-size: 46px; letter-spacing: 8px; }
  .title-bourbon  { top: 282px; font-size: 92px; letter-spacing: 3px; }
  .title-whiskey  { top: 388px; font-size: 46px; letter-spacing: 8px; }

  .fill-in {
    position: absolute;
    left: 120px;
    top: 464px;
    width: 470px;
    height: 120px;
    font-family: "Roboto Condensed", sans-serif;
    font-size: 20px;
    text-align: left;
  }
  .rule {
    position: absolute;
    height: 3px;
    background: var(--maroon);
  }
  .rule-top    { left: 0; top: 0; width: 470px; }
  .rule-proof  { left: 0; top: 58px; width: 210px; }
  .rule-bottle { left: 240px; top: 58px; width: 230px; }
  .rule-bottom { left: 0; top: 118px; width: 470px; }
  .divider {
    position: absolute;
    left: 226px;
    top: 22px;
    width: 3px;
    height: 70px;
    background: var(--maroon);
  }
  .field { position: absolute; line-height: 1; }
  .field-proof  { left: 0;   top: 18px; }
  .field-bottle { left: 244px; top: 18px; }
  .field-age    { left: 0;   top: 78px; }
  .field-volume { left: 244px; top: 78px; }

  .footer {
    position: absolute;
    left: 0;
    right: 0;
    top: 616px;
    display: flex;
    justify-content: center;
    align-items: center;
    gap: 14px;
    font-family: "Cinzel", serif;
    font-weight: 500;
    font-size: 24px;
  }
  .footer-line {
    width: 80px;
    height: 3px;
    background: var(--maroon);
  }
</style>
</head>
<body>
<main class="canvas">
  <section class="label">
    <svg class="label-shape" viewBox="0 0 720 680" aria-hidden="true">
      <defs>
        <linearGradient id="gold-foil" x1="0" y1="0" x2="1" y2="1">
          <stop offset="0" stop-color="var(--gold-deep)"/>
          <stop offset="0.3" stop-color="var(--gold-light)"/>
          <stop offset="0.6" stop-color="var(--gold-mid)"/>
          <stop offset="1" stop-color="var(--gold-deep)"/>
        </linearGradient>
      </defs>
      <path d="M0,90 A40,40 0 0 0 40,50 L120,50 Q360,0 600,50 L680,50 A40,40 0 0 0 720,90 L720,640 A40,40 0 0 0 680,680 L40,680 A40,40 0 0 0 0,640 Z"
            fill="url(#gold-foil)" stroke="var(--gold-deep)" stroke-width="4"/>
      <path d="M0,90 A40,40 0 0 0 40,50 L120,50 Q360,0 600,50 L680,50 A40,40 0 0 0 720,90 L720,640 A40,40 0 0 0 680,680 L40,680 A40,40 0 0 0 0,640 Z"
            transform="translate(16,16) scale(0.9556,0.953)"
            fill="none" stroke="var(--maroon)" stroke-width="4" vector-effect="non-scaling-stroke"/>
    </svg>

    <div class="label-content">
      <span class="brand-mark" aria-hidden="true"></span>
      <p class="brand-name">Hollow Fern</p>

      <h1 class="title title-kentucky">KENTUCKY</h1>
      <h2 class="title title-bourbon">BOURBON</h2>
      <h3 class="title title-whiskey">WHISKEY</h3>

      <div class="fill-in">
        <span class="rule rule-top"></span>
        <span class="field field-proof">PROOF</span>
        <span class="field field-bottle">BOTTLE N°</span>
        <span class="rule rule-proof"></span>
        <span class="rule rule-bottle"></span>
        <span class="divider"></span>
        <span class="field field-age">AGE</span>
        <span class="field field-volume">750ml</span>
        <span class="rule rule-bottom"></span>
      </div>

      <div class="footer">
        <span class="footer-line"></span>
        <span class="footer-text">Distillery</span>
        <span class="footer-line"></span>
      </div>
    </div>
  </section>
</main>
</body>
</html>
```